依頼概要
〇依頼の目的/概要
電子書籍(lumora)の表紙デザインをおねがいします。

〇画像サイズ
表紙サイズの理想的な寸法は2560×1600ピクセルです。
注:画像の寸法は1000×625ピクセル以上であることが必要です。
画像の最大の寸法は10000×10000ピクセルです。

〇タイトル
夜更けの庭で青い灯をさがす旅の物語です!

〇帯キャッチ

・眠ることも許されない
死にたくなるようなかゆみと痛みから
柔らかい潤いのある肌になった

・人生の波と家族とのご縁をひもといて
薬を使わずに治す

・「絶対に治る、治ったら
同じように苦しんでいる人の為に役立つ本を書こう」
・・・と決めていました。

デザイナーさんの判断で、
どれかを使ってもらっても、
または全部を使ってもらってもOKです。

〇著者 ぽんたるべカフェ 占導師 千景(柴崎奈緒)

文字の大きさと配置と色のインパクトがあって一目惚れしました。
修正依頼にも迅速な対応もありがたかったです。

初めての電子書籍の執筆と初めてのワークベリーへの仕事依頼で、
ドキドキで、いろいろ小さなわからないところだらけでした。
たくさんの提案、どれも素敵なものばかりですべての提案者の方々に
感謝の氣持ちでいっぱいです。ありがとうございました。
これからもアトピー性皮膚炎を克服するための電子書籍を執筆していく予定なので
また、協力していただけたら嬉しいです。

```html
<!DOCTYPE html>
<html lang="ja">
<head>
<meta charset="utf-8">
<title>夜更けの庭で青い灯をさがす旅の物語です!</title>
<link href="https://fonts.googleapis.com/css2?family=Noto+Sans+JP:wght@400;500;700;900&family=Noto+Serif:wght@400&family=Playfair+Display:ital@1&display=swap" rel="stylesheet">
<style>
  :root {
    --pink: #ef6f86;
    --band: #f27d8c;
    --ink: #1a1a1a;
    --white: #ffffff;
    --sky-top: #eef2f6;
    --sky-bottom: #f7f3ef;
  }
  * { margin: 0; padding: 0; box-sizing: border-box; }
  html, body { width: 750px; height: 1200px; overflow: hidden; background: var(--white); }
  .cover {
    position: relative; width: 750px; height: 1200px; overflow: hidden;
    font-family: "Noto Sans JP", sans-serif; color: var(--ink);
  }
  .cover__photo {
    position: absolute; inset: 0 0 455px 0;
    background:
      radial-gradient(ellipse 260px 360px at 560px 520px, rgba(214,200,190,.55), transparent 70%),
      linear-gradient(180deg, var(--sky-top) 0%, #f3f4f6 55%, var(--sky-bottom) 100%);
  }
  .cover__ghost {
    position: absolute; top: 18px; left: -10px; width: 770px;
    font-family: "Noto Serif", serif; font-size: 190px; letter-spacing: 6px;
    color: rgba(200,200,205,.35); white-space: nowrap; line-height: 1;
  }
  .cover__script {
    position: absolute; top: 170px; left: 560px;
    font-family: "Playfair Display", serif; font-style: italic;
    font-size: 30px; color: #444; transform: rotate(-8deg);
  }
  .title { position: absolute; top: 40px; left: 70px; font-weight: 900; line-height: 1.08; }
  .title__line { display: block; white-space: nowrap; }
  .title__line--accent { color: var(--pink); font-size: 110px; letter-spacing: -2px; }
  .title__line--dark { color: var(--ink); font-size: 92px; letter-spacing: -1px; }
  .title__particle { color: var(--ink); font-size: 66px; }
  .author { position: absolute; top: 600px; left: 82px; line-height: 1.3; }
  .author__label { font-size: 22px; font-weight: 500; }
  .author__org { font-size: 26px; font-weight: 500; }
  .author__name { font-size: 56px; font-weight: 900; letter-spacing: 2px; }
  .author__real { font-size: 24px; font-weight: 500; letter-spacing: 0; }
  .band {
    position: absolute; left: 0; right: 0; bottom: 0; height: 455px;
    background: var(--band); color: var(--white);
  }
  .band__copy {
    position: absolute; top: 28px; right: 28px; height: 410px;
    writing-mode: vertical-rl; line-height: 1.22;
  }
  .copy--lead { font-size: 52px; font-weight: 900; margin-block-end: 14px; }
  .copy--small { font-size: 19px; font-weight: 500; line-height: 1.5; margin-block-end: 30px; }
  .copy--mid { font-size: 37px; font-weight: 900; margin-block-end: 34px; }
  .copy--quote { font-size: 52px; font-weight: 900; margin-block-end: 24px; }
  .copy--note { font-size: 19px; font-weight: 500; line-height: 1.55; }
</style>
</head>
<body>
<main class="cover">
  <div class="cover__photo" role="img" aria-label="明るい空の下で両腕を後ろに広げ、顔を空に向けて深呼吸する白いウェアの女性の写真"></div>
  <div class="cover__ghost" aria-hidden="true">ATOPIC</div>
  <div class="cover__script">dermatitis</div>

  <h1 class="title">
    <span class="title__line title__line--accent">夜更けの庭</span>
    <span class="title__line title__line--accent">で青い灯<span class="title__particle">を</span></span>
    <span class="title__line title__line--dark">さがす旅の</span>
    <span class="title__line title__line--dark">物語です!</span>
  </h1>

  <div class="author">
    <p class="author__label">著者</p>
    <p class="author__org">ぽんたるべカフェ</p>
    <p class="author__name">占導師 千景<span class="author__real">(柴崎奈緒)</span></p>
  </div>

  <section class="band">
    <div class="band__copy">
      <p class="copy--lead">眠ることも<br>許されない</p>
      <p class="copy--small">死にたくなるような<br>かゆみと痛みから<br>柔らかい潤いのある肌になった</p>
      <p class="copy--mid">人生の波と<br>家族とのご縁を<br>ひもといて<br>薬を使わずに治す</p>
      <p class="copy--quote">“絶対に治る”</p>
      <p class="copy--note">治ったら同じように苦しんでいる<br>人の為に役立つ本を書こう<br>…と決めていました。</p>
    </div>
  </section>
</main>
</body>
</html>
```